Business Card Design

We need a business card design for a new dental practice in Brisbane. I'd like the basic details and logo on one side and appointment schedule on the other side. It is based in CBD office area and would prefer a professional and modern design.
Target Market(s)
20-60 years old office workers and residents with high education levels
Industry/Entity Type
Dental
Contact Information for Business Card
Harbourlight Dental
Dr Marcus Lindqvist
Principal Dentist
07 3194 6627
admin@harbourlightdentistry.example.au
www.harbourlightdentistry.example.au
S27, Level 3, Ferndale North Tower, 318 Gorrick St, Alderwood Heights, QLD 4118

```html
<!DOCTYPE html>
<html lang="en">
<head>
<meta charset="utf-8">
<title>Harbourlight Dental – Business Card</title>
<link rel="stylesheet" href="https://fonts.googleapis.com/css2?family=Open+Sans:wght@400;600;700&display=swap">
<style>
  :root {
    --backdrop: #d9d6d1;
    --card: #ffffff;
    --card-shade: #eceef0;
    --ink: #2b2f33;
    --navy: #25313d;
    --blue: #3f8fc8;
    --blue-light: #6cb4e2;
    --blue-deep: #2f79ad;
  }
  * { box-sizing: border-box; margin: 0; padding: 0; }
  html, body { width: 1200px; height: 899px; overflow: hidden; }
  body {
    background: var(--backdrop);
    font-family: "Open Sans", Arial, sans-serif;
    color: var(--ink);
  }
  .card {
    position: absolute;
    left: 100px; top: 164px;
    width: 1000px; height: 572px;
    background: radial-gradient(ellipse at 45% 55%, var(--card) 0%, var(--card) 40%, var(--card-shade) 100%);
    box-shadow: 0 10px 30px rgba(0,0,0,.25);
    overflow: hidden;
  }
  .card__swoosh { position: absolute; inset: 0; width: 100%; height: 100%; }
  .brand {
    position: absolute; left: 44px; top: 44px;
    display: flex; align-items: center; gap: 18px;
  }
  .brand__dot {
    width: 62px; height: 62px; border-radius: 50%;
    background: var(--blue);
  }
  .brand__name {
    font-size: 40px; font-weight: 400; letter-spacing: .5px;
    color: var(--blue-deep);
  }
  .contact {
    position: absolute; left: 44px; top: 214px;
    list-style: none; font-size: 19px; line-height: 1.4;
  }
  .contact__item { display: flex; align-items: flex-start; gap: 10px; }
  .contact__icon { flex: none; width: 20px; height: 20px; margin-top: 3px; }
  .holder {
    position: absolute; right: 190px; bottom: 48px;
    text-align: right; color: var(--ink);
  }
  .holder__name { font-size: 40px; font-weight: 700; line-height: 1.15; }
  .holder__title { font-size: 34px; font-weight: 400; }
</style>
</head>
<body>
  <div class="card">
    <svg class="card__swoosh" viewBox="0 0 1000 572" preserveAspectRatio="none" aria-hidden="true">
      <defs>
        <linearGradient id="panelBlue" x1="0" y1="0" x2="1" y2="1">
          <stop offset="0" stop-color="#2f6f9c"/>
          <stop offset="1" stop-color="#6cb4e2"/>
        </linearGradient>
      </defs>
      <path d="M560,0 L1000,0 L1000,572 L900,572 C880,300 760,110 560,0 Z" fill="url(#panelBlue)"/>
      <path d="M560,0 L640,0 C830,110 940,320 948,572 L900,572 C880,300 760,110 560,0 Z" fill="#25313d"/>
      <path d="M770,130 C860,230 915,360 928,520 C905,380 860,260 770,130 Z" fill="#6cb4e2"/>
    </svg>

    <div class="brand">
      <span class="brand__dot"></span>
      <span class="brand__name">Harbourlight Dental</span>
    </div>

    <ul class="contact">
      <li class="contact__item">
        <svg class="contact__icon" viewBox="0 0 20 20"><circle cx="10" cy="10" r="10" fill="#2b2f33"/><path d="M5 10.5 10 5.5l5 5h-1.6V15H11.6v-3H8.4v3H6.6v-4.5Z" fill="#fff"/></svg>
        <span>S27, Level 3, Ferndale North Tower,<br>318 Gorrick St, Alderwood Heights, QLD 4118</span>
      </li>
      <li class="contact__item">
        <svg class="contact__icon" viewBox="0 0 20 20"><circle cx="10" cy="10" r="10" fill="#2b2f33"/><path d="M7 5c1 0 1.6 2 1.6 2.6 0 .6-.9.9-.9 1.3.4 1.2 1.7 2.6 3 3 .4 0 .7-.9 1.3-.9.6 0 2.6.6 2.6 1.6 0 .8-1.2 1.9-2 1.9C9 14.5 5.5 11 5.5 7c0-.8 1-2 1.5-2Z" fill="#fff"/></svg>
        <span>07 3194 6627</span>
      </li>
      <li class="contact__item">
        <svg class="contact__icon" viewBox="0 0 20 20"><circle cx="10" cy="10" r="10" fill="#2b2f33"/><rect x="7" y="4.5" width="6" height="11" rx="1" fill="#fff"/><rect x="8" y="6" width="4" height="6.5" fill="#2b2f33"/></svg>
        <span>0412 580 339</span>
      </li>
      <li class="contact__item">
        <svg class="contact__icon" viewBox="0 0 20 20"><circle cx="10" cy="10" r="10" fill="#2b2f33"/><rect x="5" y="8" width="10" height="7" rx="1" fill="#fff"/><rect x="7" y="4.5" width="6" height="4" fill="#fff"/></svg>
        <span>07 3194 6628</span>
      </li>
      <li class="contact__item">
        <svg class="contact__icon" viewBox="0 0 20 20"><circle cx="10" cy="10" r="10" fill="#2b2f33"/><rect x="4.5" y="6.5" width="11" height="7.5" rx="1" fill="#fff"/><path d="M4.5 7 10 11l5.5-4" fill="none" stroke="#2b2f33" stroke-width="1.2"/></svg>
        <span>admin@harbourlightdentistry.example.au</span>
      </li>
      <li class="contact__item">
        <svg class="contact__icon" viewBox="0 0 20 20"><circle cx="10" cy="10" r="10" fill="#2b2f33"/><g fill="none" stroke="#fff" stroke-width="1.2"><circle cx="10" cy="10" r="5.5"/><ellipse cx="10" cy="10" rx="2.4" ry="5.5"/><path d="M4.5 10h11"/></g></svg>
        <span>www.harbourlightdentistry.example.au</span>
      </li>
    </ul>

    <div class="holder">
      <p class="holder__name">Dr Marcus Lindqvist</p>
      <p class="holder__title">Principal Dentist</p>
    </div>
  </div>
</body>
</html>
```